Etiketten für Deodorant in fester Form
Zielgruppe
Naturkosmetik
Aufgabenstellung
Dimension of the tube:
The height of the tube’s body is 53mm
The height of the lid is 20mm
The circular of the body is 126mm

```html
<!DOCTYPE html>
<html lang="fr">
<head>
<meta charset="utf-8">
<title>SOLANEL – Cosmetique Naturelle</title>
<link rel="stylesheet" href="https://fonts.googleapis.com/css2?family=Cormorant+Garamond:wght@500;600&display=swap">
<style>
  :root {
    --leaf-deep: #16221a;
    --leaf-mid: #26382a;
    --sky-haze: #4a6464;
    --cream: #f7ecda;
  }
  html, body {
    margin: 0;
    padding: 0;
    overflow: hidden;
    background: var(--leaf-deep);
  }
  .label {
    position: relative;
    width: 1200px;
    height: 800px;
    overflow: hidden;
    font-family: "Cormorant Garamond", Georgia, serif;
    color: var(--cream);
  }
  .label__backdrop {
    position: absolute;
    inset: 0;
    background:
      radial-gradient(ellipse 45% 35% at 8% 12%, var(--sky-haze) 0%, transparent 100%),
      radial-gradient(ellipse 25% 50% at 12% 85%, #3b5656 0%, transparent 100%),
      linear-gradient(160deg, var(--leaf-mid) 0%, var(--leaf-deep) 70%);
  }
  .label__arch {
    position: absolute;
    left: 0;
    top: 0;
  }
  .label__arch text {
    font-family: "Cormorant Garamond", Georgia, serif;
    font-weight: 600;
    font-size: 37px;
    fill: var(--cream);
  }
  .label__product {
    position: absolute;
    left: 0;
    width: 100%;
    top: 270px;
    margin: 0;
    text-align: center;
    font-weight: 500;
    font-size: 182px;
    line-height: 1;
    letter-spacing: 2px;
  }
  .label__ingredient {
    position: absolute;
    left: 0;
    width: 100%;
    top: 560px;
    margin: 0;
    text-align: center;
    font-weight: 600;
    font-size: 40px;
    line-height: 1;
  }
  .label__variant {
    position: absolute;
    right: 80px;
    top: 720px;
    margin: 0;
    font-weight: 500;
    font-size: 62px;
    line-height: 1;
  }
</style>
</head>
<body>
  <main class="label">
    <div class="label__backdrop" role="img" aria-label="Close-up photograph of a dark green palm frond against a misty blue-grey sky"></div>

    <svg class="label__arch" width="1200" height="200" viewBox="0 0 1200 200" aria-label="Cosmetique Naturelle">
      <path id="arch-line" d="M 360 132 Q 600 60 840 132" fill="none"/>
      <text><textPath href="#arch-line" startOffset="50%" text-anchor="middle">Cosmetique Naturelle</textPath></text>
    </svg>

    <h1 class="label__product">SOLANEL</h1>
    <p class="label__ingredient">With Cacao butter</p>
    <p class="label__variant">Sensitiv</p>
  </main>
</body>
</html>
```